Vesk Architecture

We are a architectural design and build company working between scales 1/1000 to 1/1 we want people to understand our difference from our design experience and quality.we build hotels restourants and office spaces.Our company name is Vesk architecture to mind sustainability.

We want to write our adress phone and work spesifications on the card and we want our logo as backround.

Ps:you could find the logo adress and phone box numbers from the web:www.veskmimarlik-ornek.com

Target Market(s)

Who looks for experts.

Industry/Entity Type

Architecture

Requirements
Must have
• Design is over everything.
Should not have
• we don want it to be colorfull

```html
<!DOCTYPE html>
<html lang="tr">
<head>
<meta charset="utf-8">
<title>Vesk Mimarlık — Kartvizit</title>
<link rel="stylesheet" href="https://fonts.googleapis.com/css2?family=Jost:wght@300;400;500&display=swap">
<style>
  :root {
    --backdrop: #a39f9c;
    --card-stone: #cbc6bf;
    --card-white: #ffffff;
    --ink-white: #ffffff;
    --ink-name: #6b6966;
    --ink-body: #7d7a77;
    --band-tone: #d9d6d2;
  }
  html, body {
    margin: 0;
    padding: 0;
    width: 1200px;
    height: 900px;
    overflow: hidden;
    background: var(--backdrop);
    font-family: "Jost", "Futura", sans-serif;
  }
  .canvas {
    position: relative;
    width: 1200px;
    height: 900px;
  }
  .card {
    position: absolute;
    left: 238px;
    width: 724px;
    height: 413px;
    box-sizing: border-box;
  }
  .card--front {
    top: 24px;
    background: var(--card-stone);
  }
  .card--back {
    top: 442px;
    background: var(--card-white);
  }
  .brand {
    position: absolute;
    left: 0;
    right: 0;
    top: 118px;
    text-align: center;
    color: var(--ink-white);
    font-weight: 300;
  }
  .brand__name {
    display: block;
    font-size: 150px;
    line-height: 1;
    letter-spacing: 4px;
    font-weight: 300;
  }
  .brand__sub {
    display: block;
    margin-top: 12px;
    font-size: 38px;
    letter-spacing: 6px;
    font-weight: 300;
  }
  .holder {
    position: absolute;
    left: 64px;
    top: 104px;
  }
  .holder__name {
    margin: 0;
    font-size: 23px;
    font-weight: 500;
    color: var(--ink-name);
  }
  .holder__role {
    margin: 6px 0 0;
    font-size: 15px;
    letter-spacing: 4px;
    font-weight: 400;
    color: var(--ink-name);
  }
  .contact {
    position: absolute;
    left: 363px;
    top: 168px;
    margin: 0;
    padding: 0;
    list-style: none;
    font-size: 16px;
    font-weight: 400;
    color: var(--ink-body);
  }
  .contact li {
    line-height: 34px;
  }
  .contact__label {
    font-weight: 500;
    color: var(--ink-name);
  }
  .pattern-band {
    position: absolute;
    left: 4px;
    right: 4px;
    top: 384px;
    height: 14px;
    background: var(--band-tone);
    border-radius: 7px;
  }
</style>
</head>
<body>
<main class="canvas">
  <section class="card card--front">
    <div class="brand">
      <span class="brand__name">vesk</span>
      <span class="brand__sub">MİMARLIK</span>
    </div>
  </section>

  <section class="card card--back">
    <div class="holder">
      <h1 class="holder__name">Deniz Arda KAYA</h1>
      <p class="holder__role">MIMAR</p>
    </div>
    <ul class="contact">
      <li>Yelken Mah. Liman Cad. Servi Sok.</li>
      <li>No: 7 Kadiköy / ISTANBUL</li>
      <li><span class="contact__label">t.</span> 0216 555 01 47</li>
      <li><span class="contact__label">f.</span> 0216 555 01 48</li>
      <li>e.veskmimarlik@ornekposta.com</li>
    </ul>
    <div class="pattern-band" role="img" aria-label="Decorative repeating link pattern border in light grey"></div>
  </section>
</main>
</body>
</html>
```